MIRVA Herbal throat spray for soothing and relief minor irritation

Hi there, I require a packaging design for an outer box and the label for a 30 ml round bottle.

The design of the packaging should be attractive and self explanatory along with the main context from the facade of the packaging.

-The format we expect to receive is something we can edit easily, perhaps like a CorelDraw file or perhaps photoshop or both
-We expect the turnaround time to be a week to 10 days.
- The text part is pretty much covered. oya we forgot to state "Sugar Free". please find an appropriate location.
-Please feel free to select color and visual design and also please correct the line spacing of the wording.

Attached are:
- foto of the product bottle.
-A sample of our existing product will also be attached. MIRVA BRIGHT EYE DROPS. So you can have an idea of the team color, font and Logo.

Thank you....

Dwiyan

Target Market(s)

young and mature adult who are health concious

Industry/Entity Type

health and personal hygiene

Font styles to use
Sans Serif

Colors
0094D4
00A9DD
6FCCEA
C7EBF8
E9F6FB
59FF00
82FF00
B8FF75
E3FFCB
F4FFEA
EE7325
F08F49
F5BC92
FAE3D3
FDF4ED

Requirements
Must have
• great eye catching appearance
Should not have
• please crop the "BLUE HERON" logo from MIRVA EYE DROPS and find a suitable place.

```html
<!DOCTYPE html>
<html lang="id">
<head>
<meta charset="utf-8">
<title>MIRVA Throat Spray – Label</title>
<link rel="stylesheet" href="https://fonts.googleapis.com/css2?family=Montserrat:ital,wght@0,400;0,500;0,700;0,800;0,900;1,800&display=swap">
<style>
  :root{
    --brand-green:#0b9444;
    --deep-green:#0a8a3e;
    --edge-green:#12b04a;
    --mist:#f4fbf2;
    --pale:#dcefd6;
    --ink:#111;
    --panel:rgba(255,255,255,0.55);
    --paper:#ffffff;
  }
  *{box-sizing:border-box;margin:0;padding:0}
  html,body{width:1200px;height:514px;overflow:hidden;background:var(--paper)}
  body{font-family:"Montserrat",sans-serif;position:relative}
  .label{
    position:absolute;left:0;top:0;width:1070px;height:514px;overflow:hidden;
    background:
      radial-gradient(ellipse 380px 300px at 270px 230px, #ffffff 0%, rgba(255,255,255,0) 70%),
      radial-gradient(ellipse 700px 520px at 330px 250px, rgba(255,255,255,0) 55%, rgba(255,255,255,0.7) 62%, rgba(255,255,255,0) 70%),
      linear-gradient(160deg, rgba(255,255,255,0) 70%, rgba(18,176,74,0.55) 92%, var(--edge-green) 100%),
      radial-gradient(ellipse 900px 600px at 300px 240px, var(--mist) 0%, var(--pale) 60%, #b9dfb0 100%);
  }
  .badge{position:absolute;top:37px;display:flex;align-items:flex-start;gap:4px}
  .badge svg{width:30px;height:70px;flex:none}
  .badge-text{font-weight:800;font-style:italic;font-size:35px;line-height:36px;color:var(--brand-green);letter-spacing:0.5px;margin-top:4px}
  .badge--sugar{left:72px}
  .badge--natural{left:258px}
  .brand-name{position:absolute;left:72px;top:150px;width:392px;height:96px}
  .product-pill{
    position:absolute;left:64px;top:252px;width:405px;height:50px;border-radius:24px;
    background:var(--brand-green);color:#fff;font-weight:700;font-size:47px;line-height:52px;
    text-align:center;letter-spacing:0.5px;
  }
  .tagline{position:absolute;left:64px;width:405px;top:306px;text-align:center;color:var(--brand-green);font-weight:500;font-size:33px;letter-spacing:0.3px}
  .variant-box{position:absolute;left:64px;top:367px;width:406px;height:82px;border:1.5px solid var(--brand-green);padding:8px 0 0 22px;font-size:28px;line-height:38px;color:var(--ink);font-weight:500;letter-spacing:-0.5px;white-space:nowrap}
  .volume{position:absolute;left:220px;top:462px;font-size:34px;font-weight:500;color:var(--ink)}
  .leaf-art{position:absolute;left:343px;top:468px;width:180px;height:60px}
  .info-panel{position:absolute;left:542px;top:29px;width:511px;height:466px;background:var(--panel);padding:28px 0 0 16px;color:var(--ink)}
  .info-heading{font-weight:800;font-size:17.5px;letter-spacing:0.3px}
  .info-text{font-size:18px;line-height:27.4px;font-weight:400;white-space:nowrap}
  .composition{margin-bottom:28px}
  .maker{display:flex;gap:16px;margin-top:24px;align-items:flex-start}
  .maker-mark{width:58px;display:flex;flex-direction:column;align-items:center;gap:4px;padding-top:8px}
  .maker-mark .dot{width:30px;height:30px;border-radius:50%;background:var(--brand-green)}
  .maker-mark span{font-size:11px;font-weight:700;color:var(--brand-green)}
  .registration{position:absolute;left:16px;top:428px;font-size:18px}
</style>
</head>
<body>
  <main class="label">
    <div class="badge badge--sugar">
      <svg viewBox="0 0 30 70"><path d="M28 0 C10 15 0 40 2 60 C3 70 8 70 10 66 C12 45 18 20 28 0Z" fill="var(--brand-green)"/></svg>
      <div class="badge-text">SUGAR<br>FREE</div>
    </div>
    <div class="badge badge--natural">
      <svg viewBox="0 0 30 70"><path d="M28 0 C10 15 0 40 2 60 C3 70 8 70 10 66 C12 45 18 20 28 0Z" fill="var(--brand-green)"/></svg>
      <div class="badge-text">NATURAL<br>EXTRACTS</div>
    </div>

    <svg class="brand-name" viewBox="0 0 392 96" aria-label="MIRVA">
      <text x="0" y="90" textLength="392" lengthAdjust="spacingAndGlyphs" font-family="Montserrat, sans-serif" font-weight="900" font-size="118" fill="var(--brand-green)">MIRVA</text>
    </svg>

    <div class="product-pill">THROAT SPRAY</div>
    <div class="tagline">Herbal Daily Formula</div>

    <div class="variant-box">WITH ...................................<br>.........................................</div>

    <div class="volume">30 mL</div>

    <svg class="leaf-art" role="img" aria-label="Fresh mint leaf" viewBox="0 0 180 60">
      <defs><linearGradient id="leafTone" x1="0" y1="0" x2="1" y2="1"><stop offset="0" stop-color="#5aa55a"/><stop offset="1" stop-color="#2f7a3a"/></linearGradient></defs>
      <path d="M0 60 C10 20 60 0 110 8 C140 14 165 35 180 60Z" fill="url(#leafTone)"/>
    </svg>

    <section class="info-panel">
      <h2 class="info-heading">KOMPOSISI</h2>
      <p class="info-text composition">Natrium chloida, ......................................................................</p>
      <h2 class="info-heading">REKOMENDASI PENGGUNAAN</h2>
      <p class="info-text">Cucitangan dan bersih kanhidung. Kocok botol. Buka<br>segel pengaman. Pompa beberapa kali sampai bias<br>disemprotkan. Tegakkan kepala, Semprotkan ke<br>tenggokan 2-3 kali, ulangi sesuai kebutuhan.<br>Setelah setiap penggunaan, bersihkan aplikator dan<br>tutup kembali.</p>
      <div class="maker">
        <div class="maker-mark"><div class="dot"></div><span>Sentosa</span></div>
        <p class="info-text">PT. Sentosa Herbal Nusantara<br>Bekasi Timur, Indonesia<br>www.sentosaherbal.co.id</p>
      </div>
      <p class="registration">KEMENKES RI AKD xxxxxxxxxxxx</p>
    </section>
  </main>
</body>
</html>
```